Mobil Battery Sales and Instalation

We are a automotive roadside svc company. I am looking to focus on battery sales and instalation We offer tire changes, lockuot, jump starts fuel delivry and battery sales This design should be battery sales and instalation focused My company name is. Ridgeway Roadside Svcs. 707-216-3847 call or text Hours 7am to 9pm. Free service call and instalation with purchase of new battery. Free testing Free battery disposal Colors we like are black and orange or red and black

Target Market(s)

Automotive, RV, Comerical truck, motorcycle and boat

Industry/Entity Type

Automotive

Requirements
Must have
• Pic of battery
• Mobil battery service.
Nice to have
• I want people to see this card and know its a mobil service for battery sales and installation. But can see we offer other services.
• Use my company name but i dont want that to be the standout. (Tuck it in somewhere).
Should not have
• No pictures of any trucks cars etc.
• we do not tow!

```html
<!DOCTYPE html>
<html lang="en">
<head>
<meta charset="utf-8">
<title>Ridgeway Roadside Svcs – Mobile Battery Service Card</title>
<link rel="stylesheet" href="https://fonts.googleapis.com/css2?family=Questrial&family=Tinos:wght@700&family=Roboto+Condensed:wght@400&display=swap">
<style>
  :root {
    --orange: #f47a20;
    --orange-deep: #ef5a1c;
    --orange-light: #fbb07a;
    --red: #e42a2a;
    --ink: #2b2b2b;
    --text-grey: #333333;
    --page: #e9e9e9;
    --card: #ffffff;
    --swoosh-grey: #f1f1f1;
  }
  * { box-sizing: border-box; margin: 0; padding: 0; }
  html, body {
    width: 1125px; height: 1200px; overflow: hidden;
    background: var(--page);
  }
  .canvas { position: relative; width: 1125px; height: 1200px; }

  .card {
    position: absolute; left: 40px; top: 250px;
    width: 1045px; height: 701px;
    background: var(--card);
    overflow: hidden;
    font-family: "Questrial", "Century Gothic", sans-serif;
    color: var(--text-grey);
    box-shadow: 0 6px 22px rgba(0,0,0,.18);
  }
  .card-art { position: absolute; inset: 0; }

  .brand-name {
    position: absolute; left: 64px; top: 40px;
    font-size: 72px; line-height: 1; color: var(--orange-deep);
    font-weight: 400;
  }
  .brand-sub {
    position: absolute; left: 66px; top: 134px;
    font-family: "Tinos", "Times New Roman", serif;
    font-weight: 700; font-size: 36px; color: var(--ink);
  }

  .ribbon { position: absolute; left: 60px; top: 224px; width: 320px; height: 80px; }
  .ribbon-text {
    position: absolute; left: 94px; top: 234px;
    font-size: 31px; color: #fff;
  }

  .service-list {
    position: absolute; left: 64px; top: 316px; list-style: none;
  }
  .service-list li {
    display: flex; align-items: center; gap: 16px;
    font-size: 31px; height: 46px; color: var(--text-grey);
  }
  .tick { width: 24px; height: 24px; flex: none; }

  .offer {
    position: absolute; left: 64px; top: 566px;
    font-size: 28px; line-height: 36px; color: var(--red);
  }

  .segments {
    position: absolute; left: 412px; top: 112px;
    width: 190px; height: 190px; border-radius: 50%;
    display: flex; align-items: center; justify-content: center;
    text-align: center;
    font-family: "Roboto Condensed", "Arial Narrow", sans-serif;
    font-size: 20px; line-height: 28px; color: #fff;
  }

  .contact-bar {
    position: absolute; left: 682px; height: 46px;
    background: var(--orange);
    display: flex; align-items: center; color: #fff;
    right: 0;
  }
  .contact-bar.phone { top: 43px; }
  .contact-bar.phone span { font-size: 42px; padding-left: 42px; letter-spacing: .5px; }
  .contact-bar.text { top: 104px; height: 42px; }
  .contact-bar.text span { font-size: 28px; padding-left: 42px; }
  .contact-icon {
    position: absolute; width: 50px; height: 50px; left: 658px;
  }
  .contact-icon.phone { top: 41px; }
  .contact-icon.text { top: 100px; }

  .headline {
    position: absolute; right: 55px; top: 170px;
    text-align: right; font-size: 30px; line-height: 37px; color: var(--ink);
  }

  .battery-visual {
    position: absolute; left: 570px; top: 294px;
    width: 430px; height: 320px;
    background: radial-gradient(ellipse at 50% 55%, #d9dcdf 0%, #eceef0 55%, rgba(255,255,255,0) 75%);
  }

  .perks {
    position: absolute; left: 493px; top: 632px; right: 0; height: 48px;
    display: flex; align-items: center; padding-left: 62px;
    font-size: 28px; color: #fff;
    background: var(--orange);
    clip-path: polygon(6% 0, 100% 0, 100% 100%, 0 100%);
  }
</style>
</head>
<body>
<div class="canvas">
  <section class="card">
    <svg class="card-art" viewBox="0 0 1045 701" width="1045" height="701" aria-hidden="true">
      <defs>
        <linearGradient id="swooshGrad" x1="0" y1="0" x2="1" y2="1">
          <stop offset="0" stop-color="#ef4c1c"/>
          <stop offset="1" stop-color="#f79a3a"/>
        </linearGradient>
        <radialGradient id="discGrad" cx="50%" cy="45%" r="55%">
          <stop offset="0" stop-color="#f6893a"/>
          <stop offset="1" stop-color="#ee6420"/>
        </radialGradient>
      </defs>
      <!-- soft grey sweep behind right side -->
      <path d="M560 0 H1045 V701 H520 C600 560 650 420 640 290 C630 170 600 80 560 0 Z" fill="var(--swoosh-grey)"/>
      <!-- orange swoosh -->
      <path d="M500 0 H545 C610 70 640 150 600 220 C585 180 560 80 500 0 Z" fill="url(#swooshGrad)"/>
      <path d="M470 290 C440 360 405 420 380 450 C420 400 460 350 490 300 Z" fill="var(--orange)"/>
      <!-- disc halo -->
      <circle cx="507" cy="207" r="105" fill="var(--orange-light)" opacity=".85"/>
      <circle cx="507" cy="207" r="95" fill="url(#discGrad)"/>
    </svg>

    <div class="brand-name">Ridgeway</div>
    <div class="brand-sub">Roadside Svcs.</div>

    <svg class="ribbon" viewBox="0 0 320 80" aria-hidden="true">
      <polygon points="4,0 312,0 296,28 312,56 10,56 0,28" fill="var(--red)"/>
      <polygon points="236,56 268,56 246,76" fill="var(--red)"/>
    </svg>
    <div class="ribbon-text">We are Best in</div>

    <ul class="service-list">
      <li><svg class="tick" viewBox="0 0 24 24"><circle cx="12" cy="12" r="10" fill="none" stroke="var(--orange)" stroke-width="2.4"/><path d="M7 12.5l3.5 3.5L18 8" fill="none" stroke="var(--ink)" stroke-width="2.6" stroke-linecap="round" stroke-linejoin="round"/></svg>Battery Sales</li>
      <li><svg class="tick" viewBox="0 0 24 24"><circle cx="12" cy="12" r="10" fill="none" stroke="var(--orange)" stroke-width="2.4"/><path d="M7 12.5l3.5 3.5L18 8" fill="none" stroke="var(--ink)" stroke-width="2.6" stroke-linecap="round" stroke-linejoin="round"/></svg>Battery installation</li>
      <li><svg class="tick" viewBox="0 0 24 24"><circle cx="12" cy="12" r="10" fill="none" stroke="var(--orange)" stroke-width="2.4"/><path d="M7 12.5l3.5 3.5L18 8" fill="none" stroke="var(--ink)" stroke-width="2.6" stroke-linecap="round" stroke-linejoin="round"/></svg>Tire Changes</li>
      <li><svg class="tick" viewBox="0 0 24 24"><circle cx="12" cy="12" r="10" fill="none" stroke="var(--orange)" stroke-width="2.4"/><path d="M7 12.5l3.5 3.5L18 8" fill="none" stroke="var(--ink)" stroke-width="2.6" stroke-linecap="round" stroke-linejoin="round"/></svg>Lockout</li>
      <li><svg class="tick" viewBox="0 0 24 24"><circle cx="12" cy="12" r="10" fill="none" stroke="var(--orange)" stroke-width="2.4"/><path d="M7 12.5l3.5 3.5L18 8" fill="none" stroke="var(--ink)" stroke-width="2.6" stroke-linecap="round" stroke-linejoin="round"/></svg>Jump Starts Fuel Delivery</li>
    </ul>

    <p class="offer">Free Service Call And<br>Installation With Purchase<br>Of New Battery.</p>

    <div class="segments">FOR AUTO,<br>COMMERCIAL,<br>MARINE/<br>RV,POWERSPORT</div>

    <div class="contact-bar phone"><span>707-216-3847</span></div>
    <div class="contact-bar text"><span>or text 7am to 9pm</span></div>
    <svg class="contact-icon phone" viewBox="0 0 50 50" aria-hidden="true">
      <circle cx="25" cy="25" r="23" fill="#fff"/>
      <circle cx="25" cy="25" r="19" fill="var(--red)"/>
      <path d="M18 15c1-1 2.5-1 3.2 0l2 3c.6 1 .3 2-.5 2.6l-1.4 1c.9 2.4 2.8 4.4 5.2 5.4l1-1.4c.6-.8 1.7-1 2.6-.4l3 2c1 .7 1 2.2 0 3.2l-1.4 1.4c-1.4 1.4-3.6 1.6-5.4.6-4.6-2.5-8.3-6.2-10.8-10.8-1-1.8-.8-4 .6-5.4z" fill="#fff"/>
    </svg>
    <svg class="contact-icon text" viewBox="0 0 50 50" aria-hidden="true">
      <circle cx="25" cy="25" r="23" fill="#fff"/>
      <circle cx="25" cy="25" r="19" fill="var(--red)"/>
      <path d="M15 16h20a2 2 0 0 1 2 2v11a2 2 0 0 1-2 2H23l-5 4v-4h-3a2 2 0 0 1-2-2V18a2 2 0 0 1 2-2z" fill="none" stroke="#fff" stroke-width="2"/>
      <path d="M18 21h14M18 25h10" stroke="#fff" stroke-width="2" stroke-linecap="round"/>
    </svg>

    <p class="headline">Mobil Service For<br>Battery Sales And<br>Installation</p>

    <div class="battery-visual" role="img" aria-label="Group of three car batteries in grey and black with red and blue terminals"></div>

    <div class="perks">Free Testing Free Battery Disposal</div>
  </section>
</div>
</body>
</html>
```